R. P. Pelsar & Associates, Inc

Rodrigo Pelsar
Accountant
4213 SE 87th AVE
Cedar Vale, Ohio 44120
(555) 482-0917
rod.pelsar@quillmail.net
Accounting - Tax Preparation Services - Bookkeeping
Side - one business logo on the left and business information on right
On Backside: The logo in the middle and under the logo my company name.

Rounded Corner of the cards
In reference to the logo and cards I need to adjust the circle around the RP and color.

```html
<!DOCTYPE html>
<html lang="en">
<head>
<meta charset="utf-8">
<title>R. P. Pelsar &amp; Associates, Inc — Business Cards</title>
<link rel="stylesheet" href="https://fonts.googleapis.com/css2?family=Poppins:wght@400;500;600;700&display=swap">
<style>
  :root {
    --page: #e6e7e9;
    --card: #ffffff;
    --ink: #231f20;
    --blue: #1b74c5;
    --band: #2a2627;
    --band-text: #f2f2f2;
    --faint: #efeff1;
    --rule: #3a3a3a;
  }
  * { box-sizing: border-box; margin: 0; padding: 0; }
  html, body {
    width: 1200px; height: 900px; overflow: hidden;
    background: var(--page);
    font-family: "Poppins", sans-serif;
    color: var(--ink);
  }
  .card {
    position: absolute;
    left: 250px;
    width: 700px; height: 400px;
    background: var(--card);
    border-radius: 28px;
    overflow: hidden;
    box-shadow: 0 6px 18px rgba(0,0,0,0.12);
  }
  .card--back { top: 36px; }
  .card--front { top: 464px; }

  /* Back */
  .back-lockup {
    position: absolute; inset: 0;
    display: flex; flex-direction: column; align-items: center; justify-content: center;
    gap: 22px;
  }
  .mark-circle {
    width: 130px; height: 130px; border-radius: 50%;
    border: 4px solid var(--ink);
  }
  .company-name {
    font-weight: 700; font-size: 26px; color: var(--ink);
    letter-spacing: 0.5px; text-align: center;
  }

  /* Front */
  .front-logo {
    position: absolute; left: 40px; top: 60px; width: 210px;
    display: flex; flex-direction: column; align-items: center; gap: 14px;
  }
  .front-logo .mark-circle { width: 110px; height: 110px; }
  .front-logo .company-name { font-size: 17px; line-height: 1.3; }
  .divider {
    position: absolute; left: 285px; top: 40px; width: 1.5px; height: 210px;
    background: var(--rule);
  }
  .faint-mark {
    position: absolute; right: -40px; top: 70px;
    width: 300px; height: 300px; border-radius: 50%;
    border: 10px solid var(--faint);
  }
  .contact { position: absolute; left: 320px; top: 52px; }
  .person-name { font-weight: 600; font-size: 30px; line-height: 1.1; }
  .person-name .surname { color: var(--blue); }
  .person-title { font-size: 17px; margin-bottom: 14px; }
  .contact-list { list-style: none; font-size: 17px; line-height: 1.55; }
  .contact-list li { display: flex; align-items: flex-start; gap: 10px; }
  .contact-list svg { flex: none; margin-top: 6px; fill: var(--blue); }
  .address-lines { display: block; }

  .service-band {
    position: absolute; left: 0; right: 0; bottom: 0; height: 84px;
    background: var(--band); color: var(--band-text);
    display: flex; align-items: center; justify-content: center; gap: 36px;
    font-size: 19px;
  }
  .service { display: flex; align-items: center; gap: 10px; }
  .service svg { fill: none; stroke: var(--blue); stroke-width: 2; }
</style>
</head>
<body>

<section class="card card--back" aria-label="Business card, back">
  <div class="back-lockup">
    <div class="mark-circle" aria-hidden="true"></div>
    <p class="company-name">R. P. Pelsar &amp; Associates, Inc</p>
  </div>
</section>

<section class="card card--front" aria-label="Business card, front">
  <div class="faint-mark" aria-hidden="true"></div>

  <div class="front-logo">
    <div class="mark-circle" aria-hidden="true"></div>
    <p class="company-name">R. P. Pelsar &amp;<br>Associates, Inc</p>
  </div>

  <div class="divider" aria-hidden="true"></div>

  <div class="contact">
    <h1 class="person-name">Rodrigo <span class="surname">Pelsar</span></h1>
    <p class="person-title">Accountant</p>
    <ul class="contact-list">
      <li>
        <svg width="14" height="14" viewBox="0 0 24 24" aria-hidden="true"><path d="M6.6 10.8a15.1 15.1 0 0 0 6.6 6.6l2.2-2.2a1 1 0 0 1 1-.25 11.4 11.4 0 0 0 3.6.57 1 1 0 0 1 1 1V20a1 1 0 0 1-1 1A17 17 0 0 1 3 4a1 1 0 0 1 1-1h3.5a1 1 0 0 1 1 1c0 1.25.2 2.45.57 3.57a1 1 0 0 1-.25 1z"/></svg>
        <span>(555) 482-0917</span>
      </li>
      <li>
        <svg width="16" height="14" viewBox="0 0 24 20" aria-hidden="true"><path d="M2 2h20v16H2z M2 2l10 8 10-8" fill="none" stroke="#1b74c5" stroke-width="2.4"/></svg>
        <span>rod.pelsar@quillmail.net</span>
      </li>
      <li>
        <svg width="14" height="18" viewBox="0 0 24 32" aria-hidden="true"><path d="M12 0a12 12 0 0 0-12 12c0 9 12 20 12 20s12-11 12-20A12 12 0 0 0 12 0zm0 17a5 5 0 1 1 0-10 5 5 0 0 1 0 10z"/></svg>
        <span class="address-lines">4213 SE 87th AVE<br>Cedar Vale, Ohio 44120</span>
      </li>
    </ul>
  </div>

  <div class="service-band">
    <div class="service">
      <svg width="24" height="26" viewBox="0 0 24 26" aria-hidden="true"><rect x="3" y="2" width="18" height="22" rx="2"/><rect x="6" y="5" width="12" height="5"/><path d="M7 14h2M11 14h2M15 14h2M7 18h2M11 18h2M15 18h2"/></svg>
      <span>Accounting</span>
    </div>
    <div class="service">
      <svg width="30" height="24" viewBox="0 0 30 24" aria-hidden="true"><rect x="2" y="3" width="26" height="18" rx="2"/><path d="M6 8h10M6 12h18M6 16h18"/></svg>
      <span>Tax Preparation Services</span>
    </div>
    <div class="service">
      <svg width="24" height="26" viewBox="0 0 24 26" aria-hidden="true"><rect x="4" y="2" width="16" height="22" rx="2"/><path d="M15 8h-4a2 2 0 0 0 0 4h2a2 2 0 0 1 0 4H9M12 6v12"/></svg>
      <span>Bookkeeping</span>
    </div>
  </div>
</section>

</body>
</html>
```